B2B telecom company need web design

We need a web design for our corporate web site. The company exists since almost 10 years.
This is a DESIGN contest, you're expected to provide design only, NOT the whole website. The winner will have to provide the HTML template (with Lorem Ipsum content) and the CSS files of his design.
Our initial product is SMS peering in P2P (you send a SMS to a friend in a foreign country, great chance that your operator route your SMS to us that we route to the recipient). We're launching a bulk SMS service (marketing and application to SMS).
Target is mostly corporate, usually big corporate (operators, contents providers...) where use of SMS is part of the main business.
The web site is composed of 1 landing page and 7 content pages (plan is given for your information, all content page are using the same template and the same design, you do NOT need to make one design per page) :
* About US
Company Profile
They trust us
The Vortel Team
Partners
Contact us
* Solution
P2P SMS
A2P SMS
You only need to submit the landing page and a template page for the content (with h1, h2, h3 and h4).
Design must be based on our new logo (see attached file).
Our current web site http://www.vortel-example.com
The winner of the contest will have to provide state of the art HTML template and CSS files of his design. Photo used shall be downloaded from Pixaldo (provide the ID of the picture that we purchase file).
Target Market(s)
Telecom operator. SMS Peering hubs. Bulk SMS.
Industry/Entity Type
It Company
Number of Pages Required
2 page
Look and feel

```html
<!DOCTYPE html>
<html lang="en">
<head>
<meta charset="utf-8">
<title>Vortel Mobile</title>
<link href="https://fonts.googleapis.com/css2?family=Source+Sans+3:wght@300;400;600;700&display=swap" rel="stylesheet">
<style>
:root{
  --green:#7fba25;
  --green-dark:#6da51c;
  --text:#444;
  --muted:#777;
  --light:#efefef;
  --dark:#2b2b2b;
  --footer:#333333;
  --white:#fff;
}
*{box-sizing:border-box;margin:0;padding:0}
html,body{width:1200px;height:2692px;overflow:hidden}
body{font-family:"Source Sans 3",Arial,sans-serif;color:var(--text);background:var(--white);position:relative}
.wrap{width:878px;margin:0 auto;position:relative}
.abs{position:absolute;left:0;width:1200px}

/* header */
.site-header{top:0;height:87px;background:var(--white);border-bottom:1px solid #e6e6e6}
.brand{position:absolute;left:161px;top:27px;font-size:27px;font-weight:400;color:#333;letter-spacing:.5px}
.main-nav{position:absolute;right:160px;top:0;display:flex;height:87px}
.main-nav a{font-size:11.5px;color:#666;text-decoration:none;text-transform:uppercase;padding:38px 6px 0}
.main-nav a.active{color:var(--green);background:#f2f2f2;border-top:3px solid var(--green);padding-top:35px;padding-left:10px;padding-right:10px}

/* hero */
.hero{top:87px;height:432px;background:linear-gradient(120deg,#8a9a6a 0%,#5c6e3a 40%,#3d4a25 70%,#55663a 100%)}
.hero-lines{position:absolute;left:0;top:0}
.hero-title{position:absolute;top:148px;width:1200px;text-align:center;color:var(--white);font-weight:600;font-size:27px;line-height:33px;text-transform:uppercase}
.btn{display:inline-block;background:var(--green);color:var(--white);font-weight:600;font-size:14px;text-transform:uppercase;text-align:center;text-decoration:none}
.hero .btn{position:absolute;left:488px;top:236px;width:224px;height:48px;line-height:48px}
.hero-tag{position:absolute;top:323px;width:152px;height:63px;line-height:63px;text-align:center;color:var(--white);font-weight:600;font-size:26px;background:rgba(255,255,255,.12)}

/* section headings */
.section-title{text-align:center;font-size:25px;font-weight:400;color:#444;text-transform:uppercase}
.section-title::after{content:"";display:block;width:112px;height:5px;margin:16px auto 0;border-top:2px solid var(--green);border-bottom:1px solid var(--green)}
.lead{text-align:center;font-size:12.5px;line-height:22px;color:var(--muted)}

/* welcome */
.welcome{top:519px;height:531px}
.welcome .section-title{padding-top:64px}
.welcome .lead{margin-top:40px}
.service-cards{display:flex;justify-content:space-between;margin-top:34px}
.service-card{width:415px;height:202px;position:relative;display:flex;align-items:center;justify-content:center}
.service-card.p2p{background:linear-gradient(135deg,#cfcfcf,#8c8c8c 60%,#b5b5b5)}
.service-card.a2p{background:linear-gradient(135deg,#d8d6d2,#a9a5a0 55%,#6e6860)}
.service-card h3{color:var(--white);font-size:32px;font-weight:700;padding:6px 34px;border-top:2px solid rgba(255,255,255,.8);border-bottom:2px solid rgba(255,255,255,.8)}

/* partners */
.partners{top:1050px;height:400px;background:var(--light)}
.partners .section-title{padding-top:52px}
.partners .lead{margin-top:36px}
.partner-row{display:flex;justify-content:center;gap:18px;margin-top:40px;position:relative}
.partner{width:173px;height:100px;background:var(--white);display:flex;align-items:center;justify-content:center;font-size:21px;font-weight:600;color:#333}
.partner .dot{width:12px;height:12px;border-radius:50%;background:var(--green);margin-right:8px}
.arrow{position:absolute;top:24px}
.arrow.prev{left:0}
.arrow.next{right:0}

/* cta */
.cta{top:1450px;height:208px;background:linear-gradient(90deg,#1a1a1a,#3a3a3a 55%,#222)}
.cta h2{color:var(--white);text-align:center;font-size:25px;line-height:32px;font-weight:700;text-transform:uppercase;padding-top:39px}
.cta .btn{position:absolute;left:488px;top:121px;width:224px;height:48px;line-height:48px}

/* testimonials */
.testimonials{top:1658px;height:611px}
.testimonials .section-title{padding-top:53px}
.testimonials .lead{margin-top:38px;font-size:14px;color:#444}
.testimonials .lead em{font-style:normal;color:var(--green)}
.quotes{display:flex;justify-content:space-between;margin-top:36px}
.quote{width:415px}
.quote blockquote{position:relative;background:#f2f2f2;border:1px solid #e4e4e4;height:140px;padding:22px 22px;font-size:12.5px;line-height:21px;color:#666}
.quote blockquote::after{content:"";position:absolute;left:20px;bottom:-20px;border-right:20px solid transparent;border-top:20px solid #f2f2f2}
.author{display:flex;align-items:center;margin-top:36px}
.avatar{width:62px;height:62px;border-radius:50%;background:linear-gradient(160deg,#c9c9c9,#6b6f78)}
.author div{margin-left:13px}
.author strong{display:block;color:var(--green);font-weight:400;font-size:14px}
.author small{font-size:12px;color:#444}
.pager{position:absolute;top:538px;left:578px;display:flex;gap:4px}
.pager i{width:7px;height:7px;border-radius:50%;background:#ddd}
.pager i.on{background:var(--green)}

/* newsletter */
.newsletter{top:2269px;height:162px;background:var(--green)}
.newsletter h2{color:var(--white);text-align:center;font-size:20px;font-weight:600;text-transform:uppercase;padding-top:34px}
.signup{position:absolute;left:399px;top:79px;display:flex;gap:8px}
.signup .field{width:316px;height:44px;border:1px solid var(--white);color:var(--white);font-size:12.5px;font-weight:600;padding-left:18px;line-height:42px;text-transform:uppercase}
.signup .submit{width:135px;height:44px;background:var(--white);color:var(--green);font-size:12.5px;font-weight:600;text-align:center;line-height:44px;text-transform:uppercase}

/* footer */
.site-footer{top:2431px;height:261px;background:var(--footer);color:#ccc}
.footer-links{position:absolute;left:161px;top:48px;display:grid;grid-template-columns:152px 142px 112px}
.footer-links a{display:block;color:#ccc;font-size:11px;text-transform:uppercase;text-decoration:none;padding:6px 0 7px;border-bottom:1px solid #454545}
.footer-col{position:absolute;top:44px}
.footer-col h4{color:var(--white);font-size:14px;font-weight:600;text-transform:uppercase}
.follow{left:670px}
.socials{display:flex;gap:5px;margin-top:22px}
.socials i{width:28px;height:28px;border-radius:50%;background:var(--green)}
.contact{left:881px}
.contact p{font-size:14px;margin-top:14px;line-height:22px;color:#bbb}
.contact p + p{margin-top:0;color:var(--green)}
.copyright{position:absolute;top:201px;width:1200px;text-align:center;font-size:11px;color:#aaa}
</style>
</head>
<body>

<header class="abs site-header">
  <div class="brand">Vortel Mobile</div>
  <nav class="main-nav">
    <a class="active" href="#">Home</a>
    <a href="#">About us</a>
    <a href="#">Solutions</a>
    <a href="#">Company profile</a>
    <a href="#">They trust us</a>
    <a href="#">The Vortel team</a>
    <a href="#">Partners</a>
    <a href="#">Contact us</a>
  </nav>
</header>

<section class="abs hero" role="img" aria-label="Photo of hands holding a smartphone in front of a laptop, green tinted">
  <svg class="hero-lines" width="1200" height="432" viewBox="0 0 1200 432" fill="none" stroke="#fff" stroke-width="2">
    <polyline points="342,207 263,288 263,318"/>
    <polyline points="869,207 942,288 942,318"/>
    <polyline points="200,336 200,323 215,323"/>
    <polyline points="337,323 352,323 352,336"/>
    <polyline points="200,373 200,386 215,386"/>
    <polyline points="337,386 352,386 352,373"/>
    <polyline points="856,336 856,323 871,323"/>
    <polyline points="995,323 1010,323 1010,336"/>
    <polyline points="856,373 856,386 871,386"/>
    <polyline points="995,386 1010,386 1010,373"/>
  </svg>
  <h1 class="hero-title">Build your business on the most reliable<br>global communications backbone</h1>
  <a class="btn" href="#">I want to know more</a>
  <div class="hero-tag" style="left:200px">P2P SMS</div>
  <div class="hero-tag" style="left:857px">A2P SMS</div>
</section>

<section class="abs welcome">
  <div class="wrap">
    <h2 class="section-title">Welcome to Vortel Mobile</h2>
    <p class="lead">Lorem ipsum dolor sit amet, consectetur adipiscing elit. Nunc vel elit eu dui egestas pulvinar varius ut ex. Vestibulum vitae est tempor, tincidunt ipsum eu, sollicitudin lorem. Cras vel elementum ipsum. Fusce semper, justo vitae dignissim tristique, lacus velit ornare diam, in vestibulum neque lorem a purus. Nulla volutpat eget eros non lobortis. Quisque ac quam vel ex mattis dapibus fermentum eget nisi. Nulla aliquam ullamcorper elit pellentesque maximus.</p>
    <div class="service-cards">
      <div class="service-card p2p" role="img" aria-label="Photo of a hand holding a phone over a laptop keyboard"><h3>P2P SMS</h3></div>
      <div class="service-card a2p" role="img" aria-label="Photo of a person lying down reading a phone"><h3>A2P SMS</h3></div>
    </div>
  </div>
</section>

<section class="abs partners">
  <div class="wrap">
    <h2 class="section-title">Our Partners</h2>
    <p class="lead">Fusce semper, justo vitae dignissim tristique, lacus velit ornare diam, in vestibulum neque lorem a purus. Nulla volutpat eget eros non lobortis. Quisque ac quam vel ex mattis dapibus fermentum eget nisi. Nulla aliquam ullamcorper elit pellentesque maximus.</p>
    <div class="partner-row">
      <svg class="arrow prev" width="26" height="50" viewBox="0 0 26 50" fill="none" stroke="#7fba25" stroke-width="2"><polyline points="24,2 2,25 24,48"/></svg>
      <div class="partner">Brisko</div>
      <div class="partner">Marvane</div>
      <div class="partner"><i class="dot"></i>Helpnest</div>
      <div class="partner">Tandemly</div>
      <svg class="arrow next" width="26" height="50" viewBox="0 0 26 50" fill="none" stroke="#7fba25" stroke-width="2"><polyline points="2,2 24,25 2,48"/></svg>
    </div>
  </div>
</section>

<section class="abs cta" role="img" aria-label="Dark photo of a hand using a smartphone">
  <h2>Fusce semper, justo vitae dignissim tristique, lacus velit ornare<br>diam, in vestibulum neque lorem a purus.</h2>
  <a class="btn" href="#">I want to know more</a>
</section>

<section class="abs testimonials">
  <div class="wrap">
    <h2 class="section-title">What Customers Say</h2>
    <p class="lead">Fusce semper, justo vitae dignissim tristique, lacus velit ornare diam, <em>in vestibulum neque lorem a purus.</em> Nulla volutpat eget eros non lobortis.<br>Quisque ac quam vel ex mattis dapibus fermentum eget nisi. Nulla aliquam ullamcorper elit <em>pellentesque maximus.</em></p>
    <div class="quotes">
      <figure class="quote">
        <blockquote>Fusce semper, justo vitae dignissim tristique, lacus velit ornare diam, in vestibulum neque lorem a purus. Nulla volutpat eget eros non lobortis. Quisque ac quam vel ex mattis dapibus fermentum eget nisi. Nulla aliquam ullamcorper elit pellentesque maximus.</blockquote>
        <figcaption class="author"><span class="avatar" role="img" aria-label="Portrait photo of the customer"></span><div><strong>Daniel Marsh</strong><small>CEO of Lorem Ipsum Co.</small></div></figcaption>
      </figure>
      <figure class="quote">
        <blockquote>Fusce semper, justo vitae dignissim tristique, lacus velit ornare diam, in vestibulum neque lorem a purus. Nulla volutpat eget eros non lobortis. Quisque ac quam vel ex mattis dapibus fermentum eget nisi. Nulla aliquam ullamcorper elit pellentesque maximus.</blockquote>
        <figcaption class="author"><span class="avatar" role="img" aria-label="Portrait photo of the customer"></span><div><strong>Daniel Marsh</strong><small>CEO of Lorem Ipsum Co.</small></div></figcaption>
      </figure>
    </div>
  </div>
  <div class="pager"><i></i><i></i><i class="on"></i><i></i><i></i></div>
</section>

<section class="abs newsletter">
  <h2>Subscribe to our newsletter</h2>
  <div class="signup"><div class="field">Enter your email ID</div><div class="submit">Subscribe</div></div>
</section>

<footer class="abs site-footer">
  <nav class="footer-links">
    <a href="#">Home</a><a href="#">They trust us</a><a href="#">Contact us</a>
    <a href="#">About us</a><a href="#">The Vortel team</a><a href="#">Privacy policy</a>
    <a href="#">Company profile</a><a href="#">Partners</a><a href="#">Terms &amp; conditions</a>
    <a href="#">Solutions</a>
  </nav>
  <div class="footer-col follow">
    <h4>Follow us on</h4>
    <div class="socials"><i></i><i></i><i></i></div>
  </div>
  <div class="footer-col contact">
    <h4>Contact us</h4>
    <p>+41 22 555 01 90</p>
    <p>info@vortel-example.com</p>
  </div>
  <p class="copyright">2015 © Copyright, Vortel Mobile, All Rights Reserved</p>
</footer>

</body>
</html>
```